Business Card Design For Office Furniture Clearance Company

Kestrel Office Clearance - our company name pretty much explains what we do, we clear offices for high end clients, mainly plc's and large international companies.

We require a nice looking business card that displays professionalism but without being too serious.

It would be nice to see just a little more than a conventional boring business card, make sure you add some flare.

Industry/Entity Type

Office Furniture

Contact Information for Business Card

CARD 1

Mark Holloway
Director
mark@kestrelofficeclear.co.uk
m: 07700 913528

t: 01632 960418
www.kestrelofficeclear.co.uk

Kestrel Office Clearance
Unit K4 B
3-7 Fenwick Lane
Ashworth
Larkfield
ZX9 4QT

Clear desks, clear floors… all at no cost to you.

CARD 2

Peter Donaldson
Director
peter@kestrelofficeclear.co.uk
m: 07700 927153

t: 01632 960418

Kestrel Office Clearance
Unit K4 B
3-7 Fenwick Lane
Ashworth
Larkfield
ZX9 4QT

Font styles to use
Sans Serif

Requirements
Must have
• A white background - as we have a blue logo.
Nice to have
• Nice use of the logo - play around with this and dissect it.

```html
<!DOCTYPE html>
<html lang="en">
<head>
<meta charset="utf-8">
<title>Kestrel Office Clearance – Business Card</title>
<link rel="stylesheet" href="https://fonts.googleapis.com/css2?family=Source+Sans+3:ital,wght@0,400;0,600;1,400&display=swap">
<style>
  :root {
    --brand-blue: #0b68a9;
    --ink: #4a4a4a;
    --card-white: #f4f5f7;
    --page: #e6e7e9;
  }
  * { margin: 0; padding: 0; box-sizing: border-box; }
  html, body {
    width: 1105px; height: 1200px; overflow: hidden;
    background: var(--page);
    font-family: "Source Sans 3", "Helvetica Neue", Arial, sans-serif;
  }
  .card {
    position: absolute; left: 182px;
    width: 747px; height: 426px;
  }
  .card-front { top: 119px; background: var(--card-white); }
  .card-back { top: 636px; background: var(--brand-blue); }

  .brand-mark {
    position: absolute; left: 72px; top: 88px;
    width: 240px; text-align: center;
  }
  .brand-circle {
    width: 190px; height: 190px; border-radius: 50%;
    background: var(--brand-blue); margin: 0 auto 18px;
  }
  .brand-name {
    font-size: 21px; font-weight: 600; color: var(--brand-blue);
    white-space: nowrap;
  }

  .details { position: absolute; left: 374px; top: 0; width: 330px; }
  .line { position: absolute; left: 0; white-space: nowrap; font-size: 20px; color: var(--ink); }
  .person-name { top: 44px; font-size: 27px; font-weight: 600; color: var(--brand-blue); letter-spacing: 0.3px; }
  .person-role { top: 76px; }
  .person-email { top: 103px; font-style: italic; }
  .company-name { top: 164px; font-weight: 600; color: var(--brand-blue); }
  .address-1 { top: 193px; }
  .address-2 { top: 219px; }
  .address-3 { top: 245px; }
  .contact { display: flex; align-items: center; gap: 8px; }
  .contact svg { width: 17px; height: 17px; fill: var(--brand-blue); flex: none; }
  .contact-phone { top: 302px; }
  .contact-mobile { top: 330px; }
  .contact-web { top: 357px; }
  .divider {
    position: absolute; left: 0; width: 310px;
    border-top: 2.5px dotted var(--brand-blue);
  }
  .divider-top { top: 143px; }
  .divider-bottom { top: 283px; }

  .back-mark { position: absolute; left: 0; right: 0; top: 64px; text-align: center; }
  .back-circle {
    width: 190px; height: 190px; border-radius: 50%;
    background: var(--card-white); margin: 0 auto 16px;
  }
  .back-name { font-size: 24px; font-weight: 600; color: var(--card-white); }
  .tagline {
    position: absolute; left: 0; right: 0; top: 348px; text-align: center;
    font-size: 20px; font-style: italic; color: var(--card-white);
  }
</style>
</head>
<body>
  <section class="card card-front">
    <div class="brand-mark">
      <div class="brand-circle"></div>
      <div class="brand-name">Kestrel Office Clearance</div>
    </div>
    <div class="details">
      <div class="line person-name">MARK HOLLOWAY</div>
      <div class="line person-role">DIRECTOR</div>
      <div class="line person-email">mark@kestrelofficeclear.co.uk</div>
      <div class="divider divider-top"></div>
      <div class="line company-name">Kestrel Office Clearance</div>
      <div class="line address-1">Unit K4 B, 3-7 Fenwick Lane</div>
      <div class="line address-2">Ashworth, Larkfield</div>
      <div class="line address-3">ZX9 4QT</div>
      <div class="divider divider-bottom"></div>
      <div class="line contact contact-phone">
        <svg viewBox="0 0 24 24" aria-hidden="true"><path d="M6.6 10.8a15.1 15.1 0 0 0 6.6 6.6l2.2-2.2c.3-.3.7-.4 1-.2 1.1.4 2.3.6 3.6.6.6 0 1 .4 1 1V20c0 .6-.4 1-1 1A17 17 0 0 1 3 4c0-.6.4-1 1-1h3.5c.6 0 1 .4 1 1 0 1.3.2 2.5.6 3.6.1.3 0 .7-.2 1z"/></svg>
        <span>01632 960418</span>
      </div>
      <div class="line contact contact-mobile">
        <svg viewBox="0 0 24 24" aria-hidden="true"><path d="M7 1h10a2 2 0 0 1 2 2v18a2 2 0 0 1-2 2H7a2 2 0 0 1-2-2V3a2 2 0 0 1 2-2zm0 3v14h10V4zm5 15.5a1.2 1.2 0 1 0 0 2.4 1.2 1.2 0 0 0 0-2.4z"/></svg>
        <span>07700 913528</span>
      </div>
      <div class="line contact contact-web">
        <svg viewBox="0 0 24 24" aria-hidden="true"><path d="M12 2a10 10 0 1 0 0 20 10 10 0 0 0 0-20zm-1 17.9A8 8 0 0 1 4.2 10L9 14.8v1a2 2 0 0 0 2 2zm6.9-2.5a2 2 0 0 0-1.9-1.4h-1v-3a1 1 0 0 0-1-1H8v-2h2a1 1 0 0 0 1-1V7h2a2 2 0 0 0 2-2v-.4a8 8 0 0 1 2.9 12.8z"/></svg>
        <span>www.kestrelofficeclear.co.uk</span>
      </div>
    </div>
  </section>

  <section class="card card-back">
    <div class="back-mark">
      <div class="back-circle"></div>
      <div class="back-name">Kestrel Office Clearance</div>
    </div>
    <p class="tagline">Clear desks, clear floors… all at no cost to you.</p>
  </section>
</body>
</html>
```